BrookTala UAS Business Card Design

I need a business card designed around my logo/name. I don't mind if you alter the logo slightly or have an idea to make it work different than it is. I also need a card that identifies my business by looking at the card. I am a drone operator who takes photo and video to be used for real estate listings, and mapping for construction.

Target Market(s)

Real Estate and Construction

Industry/Entity Type

Business

Contact Information for Business Card

I'd like it to be simple, but say a lot, have the "S" logo somewhere, but not doesn't have to prominent.

Font styles to use
Serif
Sans Serif

Colors
0792cd
00a990
fbed22
ffc214
f78f20
f69356
ed232b
000000
0456a4

Requirements
Must have
• "We'll get the shot you need"
• Martin Keelhaus
• Pilot / Owner
• 71 Dorrowmere Lane
• Shelton, CT 06517
• FAA 107 # 5140273
• Insured
• AeroMentor Certified
• (203) 418-5532
• brooktalauas@velmorent.com
• brooktalauas-web.com
Nice to have
• Something that hints to the client that I fly drones to take photos--I use a Korvel Aerion 4, which kind of looks like a "Y" when it is flying--I've included a few pics.
Should not have
• more than 3 colors.

```html
<!DOCTYPE html>
<html lang="en">
<head>
<meta charset="utf-8">
<title>BrookTala UAS – Business Card</title>
<link rel="stylesheet" href="https://fonts.googleapis.com/css2?family=Montserrat:wght@400;600;700;800&family=Open+Sans:wght@400;600&display=swap">
<style>
  :root {
    --stage: #2b2b2d;
    --paper: #f7f8fa;
    --brand-blue: #0456a4;
    --sky-blue: #0792cd;
    --ink: #2d2f33;
    --muted: #6b7280;
    --faint: #d7e3f0;
    --veil: rgba(247,248,250,.82);
  }
  * { box-sizing: border-box; margin: 0; padding: 0; }
  html, body { width: 1200px; height: 997px; overflow: hidden; }
  body {
    background: var(--stage);
    font-family: "Open Sans", Arial, sans-serif;
    position: relative;
  }
  .card {
    position: absolute;
    width: 560px;
    height: 320px;
    border-radius: 18px;
    overflow: hidden;
  }

  /* ---------- Contact side ---------- */
  .card-contact { left: 80px; top: 90px; background: var(--paper); }
  .rotor-field {
    position: absolute; inset: 0;
    background: radial-gradient(circle at 88% 18%, var(--faint) 0%, rgba(215,227,240,0) 22%),
                radial-gradient(circle at 80% 82%, var(--faint) 0%, rgba(215,227,240,0) 24%);
  }
  .divider { position: absolute; inset: 0; }
  .brand { display: flex; align-items: center; gap: 10px; }
  .card-contact .brand { position: absolute; left: 46px; top: 58px; }
  .brand-mark { width: 16px; height: 16px; background: var(--brand-blue); flex: none; }
  .brand-name {
    font-family: "Montserrat", Arial, sans-serif;
    font-weight: 800; font-size: 30px; letter-spacing: 2px; line-height: 1.2;
    color: var(--brand-blue); text-transform: uppercase; white-space: nowrap;
  }
  .credentials {
    position: absolute; right: 34px; top: 150px;
    text-align: right; font-size: 12px; line-height: 1.55;
    color: var(--ink); font-weight: 600;
  }
  .holder { position: absolute; left: 46px; top: 174px; }
  .holder-name {
    font-family: "Montserrat", Arial, sans-serif;
    font-size: 18px; font-weight: 400; letter-spacing: 1px; line-height: 22px;
    color: var(--brand-blue); text-transform: uppercase; white-space: nowrap;
  }
  .holder-role { font-size: 12px; color: var(--muted); margin-top: 2px; }
  .contact-list { list-style: none; margin-top: 10px; }
  .contact-list li {
    display: flex; align-items: flex-start; gap: 8px;
    font-size: 11.5px; font-weight: 600; color: var(--ink); line-height: 1.35;
    margin-bottom: 3px;
  }
  .contact-list svg { flex: none; margin-top: 1px; }

  /* ---------- Showcase side ---------- */
  .card-showcase { left: 560px; top: 500px; background: #2a7fa8; }
  .photo { position: absolute; inset: 0; }
  .photo-shore {
    background: linear-gradient(180deg, #6f9a6a 0%, #5c8db1 45%, #3f88b2 70%, #2c7499 100%);
    clip-path: polygon(0 0, 34% 0, 54% 100%, 0 100%);
  }
  .photo-estate {
    background: linear-gradient(180deg, #bcd6ec 0%, #5f8a3e 28%, #8a8170 52%, #9db07a 78%, #c9ccb4 100%);
    clip-path: polygon(35% 0, 67% 0, 88% 100%, 55% 100%);
  }
  .photo-harbor {
    background: linear-gradient(170deg, #4aa7c8 0%, #8ea17c 35%, #b9c3b5 60%, #8fd0d6 100%);
    clip-path: polygon(68% 0, 100% 0, 100% 100%, 89% 100%);
  }
  .seams { position: absolute; inset: 0; }
  .showcase-lockup {
    position: absolute; left: 120px; top: 166px;
    background: var(--veil);
    padding: 12px 22px 10px;
  }
  .showcase-lockup .brand-name { font-size: 32px; }
  .tagline {
    position: absolute; left: 120px; top: 244px;
    font-family: "Montserrat", Arial, sans-serif;
    font-weight: 700; font-size: 16px; letter-spacing: 3.5px; line-height: 1.4;
    color: var(--brand-blue); text-transform: uppercase; white-space: nowrap;
    background: var(--veil); padding: 4px 22px;
  }
</style>
</head>
<body>

<section class="card card-contact" aria-label="Business card, contact side">
  <div class="rotor-field" role="img" aria-label="Faint drone rotor graphics"></div>
  <svg class="divider" width="560" height="320" viewBox="0 0 560 320" aria-hidden="true">
    <line x1="252" y1="194" x2="524" y2="68" stroke="#0456a4" stroke-width="1.3"/>
  </svg>

  <div class="brand">
    <span class="brand-mark"></span>
    <span class="brand-name">BrookTala UAS</span>
  </div>

  <div class="credentials">
    <p>FAA 107 # 5140273</p>
    <p>Insured</p>
    <p>AeroMentor Certified</p>
  </div>

  <div class="holder">
    <h1 class="holder-name">Martin Keelhaus</h1>
    <p class="holder-role">Pilot / Owner</p>
    <ul class="contact-list">
      <li>
        <svg width="13" height="13" viewBox="0 0 13 13" aria-hidden="true"><circle cx="6.5" cy="6.5" r="6.5" fill="#0456a4"/><path d="M4 3.5l1.3 0 .6 1.6-.8.6a4 4 0 0 0 2 2l.6-.8 1.6.6 0 1.3c-3 .3-5.6-2.3-5.3-5.3z" fill="#fff"/></svg>
        (203) 418-5532
      </li>
      <li>
        <svg width="13" height="13" viewBox="0 0 13 13" aria-hidden="true"><circle cx="6.5" cy="6.5" r="6.5" fill="#0456a4"/><rect x="3.3" y="4.2" width="6.4" height="4.6" fill="none" stroke="#fff" stroke-width="1"/><path d="M3.3 4.4l3.2 2.4 3.2-2.4" fill="none" stroke="#fff" stroke-width="1"/></svg>
        brooktalauas@velmorent.com
      </li>
      <li>
        <svg width="13" height="13" viewBox="0 0 13 13" aria-hidden="true"><circle cx="6.5" cy="6.5" r="6.5" fill="#0456a4"/><path d="M6.5 2.8a2.3 2.3 0 0 1 2.3 2.3c0 1.7-2.3 4.3-2.3 4.3S4.2 6.8 4.2 5.1a2.3 2.3 0 0 1 2.3-2.3z" fill="#fff"/><circle cx="6.5" cy="5.1" r=".9" fill="#0456a4"/></svg>
        <span>71 Dorrowmere Lane<br>Shelton, CT 06517</span>
      </li>
    </ul>
  </div>
</section>

<section class="card card-showcase" aria-label="Business card, showcase side">
  <div class="photo photo-shore" role="img" aria-label="Aerial photo of a waterfront town with a pier"></div>
  <div class="photo photo-estate" role="img" aria-label="Aerial photo of a large stone estate among trees"></div>
  <div class="photo photo-harbor" role="img" aria-label="Aerial photo of a coastline and harbour"></div>
  <svg class="seams" width="560" height="320" viewBox="0 0 560 320" aria-hidden="true">
    <line x1="193" y1="0" x2="305" y2="320" stroke="#0792cd" stroke-width="5"/>
    <line x1="376" y1="0" x2="494" y2="320" stroke="#0456a4" stroke-width="5"/>
  </svg>
  <div class="showcase-lockup">
    <div class="brand">
      <span class="brand-mark"></span>
      <span class="brand-name">BrookTala UAS</span>
    </div>
  </div>
  <p class="tagline">We'll get the shot you need</p>
</section>

</body>
</html>
```